LETTERHEAD & ENVELOPE: eye-catching stationary design for our custom office furniture business

Our company recently rebranded and we are in need of new stationary. Specifically, we need branded letterhead for standard paper size (8.5” x 11”), and matching envelopes, size: #9.

All designs should incorporate our brand colors, brand typeface, and logo. Please view attached brand guidelines document for brand colors, and brand description.

Letterhead: 8.5” x 11” Must include CoralvexKTN Logo, Dorrit Falke Certified Dealer Logo, mailing address, phone number, website, and email address.

Envelope: 9.5” x 4.125” Must include CoralvexKTN Logo, mailing address, and Dorrit Falke Certified Dealer Logo.

Attached files include:

```html
<!DOCTYPE html>
<html lang="en">
<head>
<meta charset="utf-8">
<title>CoralvexKTN Stationery</title>
<link href="https://fonts.googleapis.com/css2?family=Raleway:wght@400&family=Montserrat:wght@400;500&display=swap" rel="stylesheet">
<style>
  :root {
    --brand-green: #5a7b6d;
    --dealer-red: #e4401e;
    --paper: #ffffff;
    --stage: #eef1f4;
    --ink: #222222;
    --ink-soft: #8c8c8c;
    --rule: #c8c8c8;
  }
  html, body { margin: 0; padding: 0; overflow: hidden; }
  body {
    width: 1200px; height: 1200px; position: relative;
    background: var(--stage);
    font-family: "Montserrat", Arial, sans-serif;
    color: var(--ink);
    -webkit-font-smoothing: antialiased;
  }
  .sheet { position: absolute; background: var(--paper); box-shadow: 0 2px 6px rgba(0,0,0,.12); }
  .brand-dot { position: absolute; border-radius: 50%; background: var(--brand-green); }
  .brand-name {
    position: absolute; margin: 0; font-family: "Raleway", sans-serif; font-weight: 400;
    color: var(--brand-green); line-height: 1; white-space: nowrap;
  }
  .grey-text { will-change: transform; }

  /* Letterhead */
  .letterhead { left: 49px; top: 250px; width: 483px; height: 682px; }
  .letterhead .brand-dot { left: 31px; top: 27px; width: 39px; height: 39px; }
  .letterhead .brand-name { left: 83px; top: 31px; font-size: 32px; }
  .contact {
    position: absolute; left: 342px; top: 15px; font-family: Arial, sans-serif; font-style: normal;
    font-size: 8px; line-height: 9.8px; color: #333333;
  }
  .contact-line { display: flex; align-items: center; gap: 4px; }
  .contact-line svg { width: 6px; height: 6px; fill: var(--brand-green); }
  .contact-address { margin-top: 3px; }
  .header-rule { position: absolute; left: 31px; top: 71px; width: 419px; height: 1px; background: var(--rule); }

  .recipient { position: absolute; left: 50px; top: 153px; }
  .recipient-label { font-size: 8.5px; letter-spacing: 1px; margin: 0 0 5px; }
  .recipient-name { font-size: 7.6px; font-weight: 500; margin: 0 0 4px; }
  .recipient-detail { font-size: 5.8px; color: var(--ink-soft); line-height: 10.4px; margin: 0; }
  .letter-date { position: absolute; right: 49px; top: 153px; font-size: 6px; color: var(--ink-soft); }

  .letter-body {
    position: absolute; left: 50px; top: 246px; width: 385px;
    font-size: 6px; line-height: 8.6px; color: var(--ink-soft); text-align: justify;
  }
  .letter-body p { margin: 0 0 8.6px; }

  .signature-mark { position: absolute; left: 50px; top: 482px; width: 84px; height: 16px; background: #d9d9d9; border-radius: 3px; }
  .signer-name { position: absolute; left: 49px; top: 508px; font-size: 7.6px; margin: 0; }
  .signer-title { position: absolute; left: 49px; top: 519px; font-size: 5.6px; color: var(--ink-soft); margin: 0; }

  .dealer { position: absolute; display: flex; align-items: center; gap: 5px; }
  .letterhead .dealer { right: 33px; bottom: 18px; }
  .dealer-dot { width: 15px; height: 15px; border-radius: 50%; background: var(--dealer-red); }
  .dealer-name { font-family: "Montserrat", sans-serif; font-size: 7.4px; color: var(--dealer-red); white-space: nowrap; }

  /* Envelope front */
  .envelope-front { left: 572px; top: 298px; width: 576px; height: 250px; }
  .envelope-front .brand-dot { left: 19px; top: 19px; width: 40px; height: 40px; }
  .envelope-front .brand-name { left: 72px; top: 22px; font-size: 32px; }
  .return-address { position: absolute; left: 74px; top: 57px; font-family: Arial, sans-serif; font-style: normal; font-size: 8px; line-height: 10.4px; color: #333333; }
  .envelope-front .dealer { right: 20px; bottom: 16px; }

  /* Envelope back */
  .envelope-back { left: 572px; top: 631px; width: 579px; height: 251px; }
  .flap { position: absolute; left: 0; top: 0; width: 579px; height: 74px; }
  .envelope-back .brand-dot { left: 202px; top: 18px; width: 32px; height: 32px; }
  .envelope-back .brand-name { left: 244px; top: 21px; font-size: 26px; }
</style>
</head>
<body>

<section class="sheet letterhead" aria-label="Letterhead">
  <span class="brand-dot"></span>
  <h1 class="brand-name">CoralvexKTN</h1>

  <address class="contact">
    <div class="contact-line"><svg viewBox="0 0 10 10"><path d="M2 0.5 L3.8 2.6 L2.9 3.8 Q4.2 6 6.2 7.1 L7.4 6.2 L9.5 8 L8.3 9.5 Q3.8 9 0.5 1.7 Z"/></svg>541.306.2274</div>
    <div class="contact-line"><svg viewBox="0 0 10 10"><path d="M0.5 2 H9.5 V8 H0.5 Z M1 2.5 L5 5.5 L9 2.5"/></svg>info@coralvexktn.com</div>
    <div class="contact-line"><svg viewBox="0 0 10 10"><circle cx="5" cy="5" r="4.5"/></svg>www.coralvexktn.com</div>
    <div class="contact-address">410 SE Alder Row, Suite 115<br>Eastmere, OR 97410</div>
  </address>
  <div class="header-rule"></div>

  <div class="recipient grey-text">
    <p class="recipient-label">TO</p>
    <p class="recipient-name">Selin Varga</p>
    <p class="recipient-detail">Human Resources<br>Brightmoor Inc.<br>2207-B Hollins Way, Tarrow<br>E89 USA</p>
  </div>
  <div class="letter-date grey-text">Friday, 01/01/2018</div>

  <div class="letter-body grey-text">
    <p>Thank you for your recent visit to our showroom. We were pleased to walk you through our latest seating and workstation options, and we believe several of them suit the needs of your growing team. Our designers have prepared an initial floor plan that balances open areas with quiet zones for focused work. Each piece can be finished in your choice of fabric and wood.</p>
    <p>We would be glad to arrange a second meeting to review the plan and answer any questions before delivery begins.</p>
    <p>Samples of each finish are enclosed.</p>
    <p>Installation is handled by our own crew, who will coordinate with your facilities staff to keep disruption to a minimum. Most projects of this size are completed within two weeks of order confirmation, and every item is covered by our full product warranty and ongoing service support.</p>
    <p>Please review the enclosed quote at your convenience. Pricing is valid for sixty days and includes delivery, assembly and removal of packaging. If you would like to adjust quantities or finishes, our team can update the proposal within one business day.</p>
    <p>We look forward to working with you.</p>
  </div>

  <div class="signature-mark" role="img" aria-label="Handwritten signature of Owen Redfield"></div>
  <p class="signer-name">Owen Redfield</p>
  <p class="signer-title grey-text">Managing Director</p>

  <div class="dealer">
    <span class="dealer-dot"></span>
    <span class="dealer-name">Dorrit Falke Certified Dealer</span>
  </div>
</section>

<section class="sheet envelope-front" aria-label="Envelope front">
  <span class="brand-dot"></span>
  <h2 class="brand-name">CoralvexKTN</h2>
  <address class="return-address">410 SE Alder Row, Suite 115<br>Eastmere, OR 97410</address>
  <div class="dealer">
    <span class="dealer-dot"></span>
    <span class="dealer-name">Dorrit Falke Certified Dealer</span>
  </div>
</section>

<section class="sheet envelope-back" aria-label="Envelope back">
  <svg class="flap" viewBox="0 0 579 74" aria-hidden="true">
    <path d="M0 0 L18 52 Q24 69 46 69 L531 69 Q553 69 560 52 L579 0 Z" fill="#ffffff" stroke="#e2e2e2" stroke-width="1"/>
  </svg>
  <span class="brand-dot"></span>
  <h2 class="brand-name">CoralvexKTN</h2>
</section>

</body>
</html>
```